Environmental Consultancy needs new professional Word Template for reporting

A professional looking word template that we can use for all of our reporting.

Word template needs:
- a full scale title page that we can include a different photograph on for each new project, our company logo, title, date, and client details
- Include four layered Headings, table of contents page.
- Each page (except title page) needs to be numbered, with the title of the report at the bottom of the page.
- each page needs our company logo at the top.
- Prefer it to be using similar colours to what we are currently using. Though open to new colours if you come up with something that suits what we do.

Our business is an environment/ecological consultancy and we provide a number of field and reporting based services to mining companies, government agencies, commercial developers, landholders, tourism operators etc. Some of the work we do includes:
- vegetation surveys and reporting
- fauna trapping surveys, and reporting
- water quality and aquatic ecosystem monitoring and reporting
- fish and macroinvertebrate surveys
- seagrass and coral surveys
- environmental impact statements
- environmental offsets
- rehabilitation design and monitoring
- monitoring design programs
- ecological constraints surveys.

I have attached our company logo, a copy of our current title page, and an extract of our current report style (has been greatly reduced and with client information removed). I would like sometime similar to this report style please.

Target Market(s)

Client and Government approval agencies

Industry/Entity Type

Environmental Consultant

Font styles to use
Sans Serif

Colors
faa54b
9bcb3c
00a990
83c9e6
85acd3

Requirements
Must have
• Word template needs:

```html
<!DOCTYPE html>
<html lang="en">
<head>
<meta charset="utf-8">
<title>Receiving Environment – Report Template</title>
<link href="https://fonts.googleapis.com/css2?family=Antonio:wght@300;400;600;700&family=PT+Sans+Narrow:wght@400;700&display=swap" rel="stylesheet">
<style>
  :root{
    --brown:#9c5b26;
    --ochre:#c27a38;
    --rule:#c9a27a;
    --band:#f6e8cc;
    --ink:#3b3b3b;
    --cover-a:#f4e2b8;
    --cover-b:#e9c98c;
    --cream:#f7ecd6;
    --paper:#ffffff;
  }
  *{box-sizing:border-box;margin:0;padding:0}
  html,body{width:1200px;height:1200px;overflow:hidden;background:#fff}
  .canvas{position:relative;width:1200px;height:1200px;overflow:hidden}

  /* ---------- generic report page (base 430 x 607) ---------- */
  .page{position:absolute;width:430px;height:607px;background:var(--paper);
    box-shadow:0 6px 20px rgba(0,0,0,.16);transform-origin:0 0;overflow:hidden;
    font-family:"PT Sans Narrow",sans-serif;color:var(--ink)}
  .page > *{position:absolute}
  .frame{left:34px;top:41px;width:288px;height:50px;border-top:1px solid var(--rule);
    border-left:1px solid var(--rule);border-top-left-radius:8px}
  .frame-foot{left:34px;top:88px;width:36px;height:8px;border-left:1px solid var(--rule);
    border-bottom:1px solid var(--rule);border-bottom-left-radius:8px}
  .brand{left:327px;top:35px;font-size:8px;color:var(--brown);white-space:nowrap}
  .page-title{left:50px;top:54px;font-family:"Antonio",sans-serif;font-weight:700;
    font-size:30px;line-height:1;color:var(--brown);letter-spacing:.3px}
  .page-title .num{margin-right:14px}
  .section-head{font-family:"Antonio",sans-serif;font-weight:600;font-size:9.5px;color:var(--ochre);
    letter-spacing:.1px;white-space:nowrap}
  .section-head::before{content:"";display:inline-block;width:7px;height:7px;background:var(--ochre);
    margin-right:5px;vertical-align:0}
  .sub-head{font-size:6.6px;line-height:10px;color:var(--ochre);font-weight:700}
  .body-text{font-size:6.6px;line-height:10px;text-align:justify}
  .body-text .dash{padding-left:8px}
  .caption{font-size:4.6px;line-height:6.4px;text-align:right;width:56px}
  .folio{left:300px;top:556px;width:66px;text-align:right;font-size:5px;line-height:6px;
    color:var(--ochre);padding-right:5px;border-right:1px solid var(--rule)}
  .folio-num{left:380px;top:552px;font-family:"Antonio",sans-serif;font-weight:700;font-size:14px;color:var(--brown)}

  /* table */
  .data-table{left:102px;top:223px;width:287px;border-collapse:collapse;font-size:6.1px;line-height:8.4px}
  .data-table th{text-align:left;font-weight:700;padding:0 0 3px;border-bottom:1px solid var(--rule)}
  .data-table td{vertical-align:top;padding:2px 0 4px}
  .data-table .band td{background:var(--band);padding:2px 4px;font-size:6px}
  .data-table tr.last td{border-bottom:1px solid var(--rule)}
  .table-cap{left:30px;top:225px;width:58px;text-align:right;font-size:4.8px;line-height:6.4px}
  .table-cap b{display:block}

  /* photo placeholders */
  .photo.satellite{background:radial-gradient(ellipse at 55% 55%,#b77a45 0 22%,transparent 40%),
    linear-gradient(160deg,#2c4a6b,#dfe6ee 35%,#3a5d84 65%,#e8eef4)}
  .photo.fire{background:linear-gradient(180deg,#4a4a42 0%,#6b5a3e 40%,#d87a22 70%,#f0a33a 85%,#6a3a1a 100%)}
  .photo.gum{background:linear-gradient(180deg,#c9a476 0%,#b87440 30%,#8a5a3c 55%,#d7b28a 80%,#c9a073 100%)}

  /* ---------- cover ---------- */
  .cover{position:absolute;left:50px;top:42px;width:462px;height:652px;
    background:linear-gradient(180deg,var(--cover-a) 0%,#f1d9a7 55%,var(--cover-b) 100%);
    box-shadow:0 8px 22px rgba(0,0,0,.2);overflow:hidden;font-family:"PT Sans Narrow",sans-serif}
  .cover > *{position:absolute}
  .cover-brand{left:301px;top:60px;font-size:19px;color:var(--brown);white-space:nowrap}
  .cover-map{left:0;top:233px;width:230px;height:250px;
    background:radial-gradient(ellipse at 55% 50%,rgba(232,200,140,.55),rgba(232,200,140,0) 70%)}
  .cover-rule{left:166px;top:265px;width:296px;height:1px;background:var(--rule)}
  .cover-photo{left:166px;top:269px;width:296px;height:173px;
    background:linear-gradient(180deg,#5f86b4 0%,#a9bfd6 35%,#d9b487 60%,#9a5b2f 80%,#5a3a22 100%)}
  .cover-title{left:225px;font-family:"Antonio",sans-serif;font-weight:700;font-size:39px;line-height:1;
    letter-spacing:1px;white-space:nowrap}
  .cover-title.light{top:401px;color:#fff}
  .cover-title.dark{top:435px;color:var(--brown)}
  .cover-sub{left:226px;top:482px;font-family:"Antonio",sans-serif;font-weight:600;font-size:11.2px;line-height:1;
    color:var(--brown);letter-spacing:.4px;white-space:nowrap}
  .cover-prep{left:303px;top:543px;height:47px;border-left:1px solid var(--brown);padding-left:9px;
    font-family:"Antonio",sans-serif;color:var(--brown);line-height:1.2}
  .cover-prep .lead{font-size:11px;font-weight:300}
  .cover-prep .client{font-size:13px;font-weight:700}
  .cover-prep .date{font-size:12px;font-weight:400}
  .cover-prep .date span{font-weight:300;font-size:10.5px}

  /* recommendations page */
  .page.tinted{background:var(--cream)}
  .rec-photo{left:252px;top:0;width:178px;height:607px}
  .rec-veil{left:252px;top:0;width:52px;height:607px;background:rgba(247,236,214,.55)}
  .page.tinted .brand{color:#f3e6cf}
  .page.tinted .folio{color:#fff;border-right-color:#fff}
  .page.tinted .folio-num{color:#fff}
  .narrow{width:134px}
</style>
</head>
<body>
<div class="canvas">

  <!-- Suitably qualified person (large, behind) -->
  <section class="page" style="left:506px;top:-140px;transform:scale(1.142)">
    <div class="frame"></div><div class="frame-foot"></div>
    <div class="brand">Gumleaf Ecology</div>
    <h1 class="page-title" style="left:77px;top:58px;line-height:1.02">SUITABLY QUALIFIED<br>PERSON</h1>
    <div class="body-text" style="left:102px;top:140px;width:287px">
      <p>This proposal has been prepared by a suitably qualified person. I hold relevant environmental qualifications from recognised Australian institutions. These qualifications include a Bachelor of Science with Honours and a Masters of Environmental Management.</p>
      <p>I have also completed regional ecosystem training through Northern Coast University, Queensland. I have over ten years experience in conducting ecological surveys and research projects within Queensland, in which I have led surveys and accompanied other ecologists with over ten years experience.</p>
      <p>&nbsp;I have also previously had the State Herbarium retain my collected plant specimens to be incorporated into their collection.</p>
      <p>Gumleaf Ecology is a registered scientific user with ethics approval, from the Department of Primary Industries (DPI) Animal Ethics Committee (AEC), able to conduct flora and fauna surveys in Queensland. This environmental assessment was conducted under Scientific Purposes Permit number</p>
    </div>
    <div style="left:102px;top:293px;font-size:6.8px;line-height:10px"><b>Clara Whitfield</b><br>BSc (Hons) MEnvMan</div>
    <div class="caption" style="left:31px;top:331px">Image description image description image sample description image description sample text here and there</div>
    <div class="photo satellite" role="img" aria-label="Satellite image of Australia with an atmospheric river" style="left:102px;top:331px;width:286px;height:210px"></div>
    <div class="folio">RECEIVING<br>ENVIRONMENT</div><div class="folio-num">3</div>
  </section>

  <!-- Cover -->
  <section class="cover">
    <div class="cover-map" role="img" aria-label="Faint map of Australia"></div>
    <div class="cover-brand">Gumleaf Ecology</div>
    <div class="cover-rule"></div>
    <div class="cover-photo" role="img" aria-label="Gum tree at sunset in front of a mountain range"></div>
    <div class="cover-title light">RECEIVING</div>
    <div class="cover-title dark">ENVIRONMENT</div>
    <div class="cover-sub">MONITORING PROGRAM - FIELD RESULTS REPORT</div>
    <div class="cover-prep">
      <div class="lead">Prepared on behalf of</div>
      <div class="client">client name</div>
      <div class="date">2020 <span>august</span></div>
    </div>
  </section>

  <!-- Results page (large) -->
  <section class="page" style="left:725px;top:53px">
    <div class="frame"></div><div class="frame-foot"></div>
    <div class="brand">Gumleaf Ecology</div>
    <h1 class="page-title"><span class="num">3</span>RESULTS</h1>
    <h2 class="section-head" style="left:78px;top:143px">3.1. DESKTOP ASSESSMENT</h2>
    <div class="sub-head" style="left:102px;top:162px">3.1.1<br>Database Overview</div>
    <p class="body-text" style="left:102px;top:193px;width:287px">A summary of the maps and databases applicable to the development area, that were reviewed as part of the desktop assessment, have been provided in Table 4.</p>
    <div class="table-cap"><b>Table 4</b>Assessment of database information</div>
    <table class="data-table">
      <colgroup><col style="width:62px"><col style="width:145px"><col style="width:36px"><col style="width:44px"></colgroup>
      <tr><th>Data Base Source</th><th>Search Results</th><th>Applicable</th><th>Reference</th></tr>
      <tr class="band"><td colspan="4">LOCAL</td></tr>
      <tr><td>City Plan – Natural Assets Overlay Map</td><td>The development area is mapped as having ‘high’ environmental importance, with the waterway mapped as ‘very high’ on the Natural Assets Overlay mapping.</td><td>&nbsp;&nbsp;Yes</td><td>Map 5, Appendix 1</td></tr>
      <tr class="band"><td colspan="4">STATE</td></tr>
      <tr class="last"><td>Regulated Vegetation Management Map</td><td>Category B (remnant vegetation) was mapped throughout the majority of the development area. Two patches of Category X (exempt) were mapped in the north, and east to south of the development area.</td><td>&nbsp;&nbsp;Yes</td><td>Appendix 3, Vegetation Management Property Report</td></tr>
    </table>
    <div class="sub-head" style="left:102px;top:345px">3.1.2<br>State Mapped Vegetation Communities</div>
    <p class="body-text" style="left:102px;top:375px;width:287px">Following the desktop review, the likelihood of occurrence for each identified threatened flora and fauna species was determined based on habitat suitability. This likelihood of occurrence assessment determined which species were considered ‘likely’, ‘possible’ or ‘unlikely’ to occur based on all desktop available information including existing confirmed records of threatened species, suitability of habitat present, location of ‘high risk areas’ mapped in the Flora Survey Trigger mapping and professional judgement.</p>
    <div class="sub-head" style="left:102px;top:436px">3.1.3<br>Significant Flora</div>
    <div class="body-text" style="left:102px;top:466px;width:287px">
      <p>Four terms for the likelihood of occurrence were used: Confirmed, Likely, Possible, and Unlikely. Following this likelihood of occurrence assessment and the field survey, an assessment of potential impacts from the proposed clearing was also undertaken to determine which threatened species would most likely be impacted by the proposed development should they be present. The results of this assessment have been provided in Appendix 7.</p>
      <p>The threatened species that were considered confirmed or likely to occur, pose the greatest constraints to the proposed development, and hence the field survey targeted the preferred habitat for these species to determine their presence.</p>
    </div>
    <div class="folio">RECEIVING<br>ENVIRONMENT</div><div class="folio-num">7</div>
  </section>

  <!-- Bottom row: page 3 -->
  <section class="page" style="left:54px;top:778px;transform:scale(.594)">
    <div class="frame"></div><div class="frame-foot"></div>
    <div class="brand">Gumleaf Ecology</div>
    <h1 class="page-title" style="left:77px;top:58px;line-height:1.02">SUITABLY QUALIFIED<br>PERSON</h1>
    <div class="body-text" style="left:102px;top:140px;width:287px">
      <p>This proposal has been prepared by a suitably qualified person. I hold relevant environmental qualifications from recognised Australian institutions. These qualifications include a Bachelor of Science with Honours and a Masters of Environmental Management.</p>
      <p>I have also completed regional ecosystem training through Northern Coast University, Queensland. I have over ten years experience in conducting ecological surveys and research projects within Queensland, in which I have led surveys and accompanied other ecologists with over ten years experience.</p>
      <p>&nbsp;I have also previously had the State Herbarium retain my collected plant specimens to be incorporated into their collection.</p>
      <p>Gumleaf Ecology is a registered scientific user with ethics approval, from the Department of Primary Industries (DPI) Animal Ethics Committee (AEC), able to conduct flora and fauna surveys in Queensland. This environmental assessment was conducted under Scientific Purposes Permit number</p>
    </div>
    <div style="left:102px;top:293px;font-size:6.8px;line-height:10px"><b>Clara Whitfield</b><br>BSc (Hons) MEnvMan</div>
    <div class="caption" style="left:31px;top:331px">Image description image description image sample description image description sample text here and there</div>
    <div class="photo satellite" role="img" aria-label="Satellite image of Australia with an atmospheric river" style="left:102px;top:331px;width:286px;height:210px"></div>
    <div class="folio">RECEIVING<br>ENVIRONMENT</div><div class="folio-num">3</div>
  </section>

  <!-- Bottom row: introduction page -->
  <section class="page" style="left:336px;top:778px;transform:scale(.594)">
    <div class="frame"></div><div class="frame-foot"></div>
    <div class="brand">Gumleaf Ecology</div>
    <div class="body-text" style="left:101px;top:58px;width:287px">
      <p>The development area is relatively flat with low relief. Elevations over the development area range from 15 m AHD to 20 m AHD, with a hill to the east of the development area that reaching an elevation of 105 m AHD (Map 10, Appendix 1). The development area is on an alluvial plain characterised by sandy loam soils.</p>
      <p>The development area is currently bushland, that has previously been used for four-wheel driving and camping. The area of the property that remains undeveloped, is mostly vegetated with remnant vegetation that comprises open woodland and riparian vegetation. The remnant vegetation contains three regional ecosystems (RE 11.3.35, RE 11.3.12 and RE 11.12.9) that are considered ‘least concern’ under the Vegetation Management Act (Map 6, Appendix 1).</p>
      <p>The development is surrounded on all sides by urban development, most of which could be considered rural (low density) residential development. No world heritage areas or other protected areas are in the vicinity of the proposed development, nor within 5 km of the proposed development.</p>
    </div>
    <h2 class="section-head" style="left:78px;top:174px">1.4 OBJECTIVES</h2>
    <div class="body-text" style="left:101px;top:193px;width:287px">
      <p>The objectives of the environmental assessment were to:</p>
      <p class="dash">– assess the environmental values of the development area and identify matters of environmental significance (MES) that might be impacted by the proposed vegetation clearing;</p>
      <p class="dash">– assess potential impacts to MES resulting from the proposed vegetation clearing;</p>
      <p class="dash">– provide mitigation measures and recommendations to minimise impacts to MES;</p>
      <p class="dash">– assess whether the development complies with assessment benchmarks provided in the Natural Assets Overlay Code of the City Plan and the State Code 16: Native Vegetation Clearing.</p>
    </div>
    <h2 class="section-head" style="left:78px;top:276px">1.5. PROJECT SCOPE</h2>
    <p class="body-text" style="left:101px;top:293px;width:287px">This environmental assessment involved a desktop review of available information, and a field survey to verify the following information:</p>
    <div class="caption" style="left:30px;top:334px">Forest fires summer 2020 image description image description</div>
    <div class="photo fire" role="img" aria-label="Firefighters working beside a bushfire" style="left:101px;top:334px;width:287px;height:210px"></div>
    <div class="folio">RECEIVING<br>ENVIRONMENT</div><div class="folio-num">8</div>
  </section>

  <!-- Bottom row: results page -->
  <section class="page" style="left:615px;top:778px;transform:scale(.594)">
    <div class="frame"></div><div class="frame-foot"></div>
    <div class="brand">Gumleaf Ecology</div>
    <h1 class="page-title"><span class="num">3</span>RESULTS</h1>
    <h2 class="section-head" style="left:78px;top:143px">3.1. DESKTOP ASSESSMENT</h2>
    <div class="sub-head" style="left:102px;top:162px">3.1.1<br>Database Overview</div>
    <p class="body-text" style="left:102px;top:193px;width:287px">A summary of the maps and databases applicable to the development area, that were reviewed as part of the desktop assessment, have been provided in Table 4.</p>
    <div class="table-cap"><b>Table 4</b>Assessment of database information</div>
    <table class="data-table">
      <colgroup><col style="width:62px"><col style="width:145px"><col style="width:36px"><col style="width:44px"></colgroup>
      <tr><th>Data Base Source</th><th>Search Results</th><th>Applicable</th><th>Reference</th></tr>
      <tr class="band"><td colspan="4">LOCAL</td></tr>
      <tr><td>City Plan – Natural Assets Overlay Map</td><td>The development area is mapped as having ‘high’ environmental importance, with the waterway mapped as ‘very high’ on the Natural Assets Overlay mapping.</td><td>&nbsp;&nbsp;Yes</td><td>Map 5, Appendix 1</td></tr>
      <tr class="band"><td colspan="4">STATE</td></tr>
      <tr class="last"><td>Regulated Vegetation Management Map</td><td>Category B (remnant vegetation) was mapped throughout the majority of the development area. Two patches of Category X (exempt) were mapped in the north, and east to south of the development area.</td><td>&nbsp;&nbsp;Yes</td><td>Appendix 3, Vegetation Management Property Report</td></tr>
    </table>
    <div class="sub-head" style="left:102px;top:345px">3.1.2<br>State Mapped Vegetation Communities</div>
    <p class="body-text" style="left:102px;top:375px;width:287px">Following the desktop review, the likelihood of occurrence for each identified threatened flora and fauna species was determined based on habitat suitability. This likelihood of occurrence assessment determined which species were considered ‘likely’, ‘possible’ or ‘unlikely’ to occur based on all desktop available information including existing confirmed records of threatened species, suitability of habitat present, location of ‘high risk areas’ mapped in the Flora Survey Trigger mapping and professional judgement.</p>
    <div class="sub-head" style="left:102px;top:436px">3.1.3<br>Significant Flora</div>
    <div class="body-text" style="left:102px;top:466px;width:287px">
      <p>Four terms for the likelihood of occurrence were used: Confirmed, Likely, Possible, and Unlikely. Following this likelihood of occurrence assessment and the field survey, an assessment of potential impacts from the proposed clearing was also undertaken to determine which threatened species would most likely be impacted by the proposed development should they be present. The results of this assessment have been provided in Appendix 7.</p>
      <p>The threatened species that were considered confirmed or likely to occur, pose the greatest constraints to the proposed development, and hence the field survey targeted the preferred habitat for these species to determine their presence.</p>
    </div>
    <div class="folio">RECEIVING<br>ENVIRONMENT</div><div class="folio-num">7</div>
  </section>

  <!-- Bottom row: recommendations page -->
  <section class="page tinted" style="left:902px;top:778px;transform:scale(.594)">
    <div class="photo gum rec-photo" role="img" aria-label="Gum tree trunk with a mountain at sunset"></div>
    <div class="rec-veil"></div>
    <div class="frame"></div><div class="frame-foot"></div>
    <div class="brand">Gumleaf Ecology</div>
    <h1 class="page-title"><span class="num">5</span>RECOMMENDATIONS</h1>
    <h2 class="section-head" style="left:79px;top:143px">5.1 HABITAT MANAGEMENT</h2>
    <div class="sub-head" style="left:103px;top:162px">5.1.1<br>Conservation significant flora and fauna species</div>
    <div class="body-text narrow" style="left:103px;top:191px">
      <p>As no conservation significant flora and fauna were recorded during the field survey, it is unlikely that impacts to these will occur as a result of clearing. Should any threatened fauna species be present in the area during clearing activities, impacts are considered unlikely due to:</p>
      <p class="dash">– The remnant vegetation and habitat to be cleared is small compared to the greater remnant area. The remnant clearing area was calculated to be 4.4 hectares.</p>
      <p class="dash">– Clearing activities will take place in a staged fashion, allowing native fauna that is displaced to relocate to new areas.</p>
    </div>
    <div class="sub-head" style="left:103px;top:332px">5.1.2<br>Special least concern species</div>
    <div class="body-text narrow" style="left:103px;top:363px">
      <p>Two flora species listed as special least concern under the NC Act were recorded within the development area.</p>
      <p>This environmental assessment involved a desktop review of available information, and a field survey to verify the following information:</p>
      <p class="dash">– The environmental values of the project site.</p>
      <p class="dash">– The vegetation communities and associated regional ecosystems (RE) present, their size and condition.</p>
    </div>
    <div class="sub-head" style="left:103px;top:473px">5.1.3<br>Least concern species</div>
    <div class="body-text narrow" style="left:103px;top:504px">
      <p>Presence of and/or presence of suitable habitat for EVNT or otherwise significant flora and fauna.</p>
      <p>This environmental assessment report includes the</p>
    </div>
    <div class="folio">RECEIVING<br>ENVIRONMENT</div><div class="folio-num">8</div>
  </section>

</div>
</body>
</html>
```